Business Card Design

We would like a colorful, engaging, welcoming business card, utilizing our picture of a local lighthouse. We are a Church. We would like the design to mostly feature the colour blue.
Thank you so much to all Designers who sent in submissions to us - it was really hard to make a decision, they were all of such high quality. We would not hesitate to recommend Sketch Harbor to other churches/ businesses.
Kestrel Beacon Fellowship
Industry/Entity Type
Business
Contact Information for Business Card
Kestrel Beacon Fellowship Inc, 17 Merrow Rd, TALLOWVALE WA 6412, Ph: (08) 9517 4063, E: beaconfellowship@quorvex.example, Friendwall logo - Kestrel Beacon Fellowship Inc, Sunday Service 10am, "For God sent not his Son into the world to condemn the world; but that the world through Him might be saved." John 3:17.

```html
<!DOCTYPE html>
<html lang="en">
<head>
<meta charset="utf-8">
<title>Kestrel Beacon Fellowship Inc – Business Card</title>
<link rel="stylesheet" href="https://fonts.googleapis.com/css2?family=Arimo:wght@400;700&display=swap">
<style>
  :root {
    --page-bg: #d9dbe0;
    --sky-top: #1a2a86;
    --sky-mid: #2b44b3;
    --sea-line: #1b2a6e;
    --hill-dark: #1d2a2c;
    --hill-green: #3b4f38;
    --text-white: #ffffff;
    --label-yellow: #f2e21a;
    --rule: #ffffff;
  }
  html, body {
    margin: 0;
    width: 1200px;
    height: 1200px;
    overflow: hidden;
    background: var(--page-bg);
    font-family: "Arimo", Arial, sans-serif;
  }
  .card {
    position: absolute;
    left: 60px;
    top: 290px;
    width: 1080px;
    height: 620px;
    overflow: hidden;
    box-shadow: 0 10px 30px rgba(0,0,0,.25);
  }
  .card__photo {
    position: absolute;
    inset: 0;
    background:
      radial-gradient(circle at 30% 22%, rgba(200,220,255,.55) 0, rgba(120,150,255,.2) 90px, rgba(0,0,0,0) 200px),
      linear-gradient(180deg, var(--sky-top) 0%, var(--sky-mid) 32%, var(--sea-line) 46%, var(--hill-green) 62%, var(--hill-dark) 100%);
  }
  .card__name {
    position: absolute;
    top: 48px;
    right: 80px;
    margin: 0;
    color: var(--text-white);
    font-weight: 700;
    font-size: 42px;
    line-height: 1.12;
    text-align: center;
    letter-spacing: .5px;
  }
  .card__contact {
    position: absolute;
    left: 80px;
    top: 345px;
    color: var(--text-white);
    font-size: 27px;
    line-height: 1;
  }
  .contact__address {
    display: inline-block;
    padding-bottom: 8px;
    border-bottom: 2px solid var(--rule);
    padding-right: 14px;
  }
  .contact__line {
    margin: 20px 0 0;
  }
  .contact__label {
    color: var(--label-yellow);
    font-weight: 700;
  }
  .card__social {
    position: absolute;
    right: 80px;
    top: 470px;
    color: var(--text-white);
    font-size: 25px;
  }
  .social__name {
    font-weight: 700;
  }
</style>
</head>
<body>
  <section class="card">
    <div class="card__photo" role="img" aria-label="Night photograph of a local lighthouse on a hilltop with shining beams, blue sky and coastal scrub"></div>
    <h1 class="card__name">KESTREL BEACON<br>FELLOWSHIP INC</h1>
    <div class="card__contact">
      <span class="contact__address">17 Merrow Rd, TALLOWVALE WA 6412</span>
      <p class="contact__line"><span class="contact__label">Phone</span> : (08) 9517 4063</p>
      <p class="contact__line"><span class="contact__label">Email</span> : beaconfellowship@quorvex.example</p>
    </div>
    <p class="card__social">Catch us on <span class="social__name">Friendwall</span></p>
  </section>
</body>
</html>
```